Illustration Design Project-infographic

This is going to be a high profile infographic about the Events Industry, to be shared as a follow up the session I led at North Harbor Summit.

Attached is the initial core of the info to be in the graphic, which will also need an extended version, as described in my brief.

This infographic project is for a high profile visual to convey information about the way that new technologies are changing the world of business to business events such as conferences.

What I have now is a spreadsheet showcasing some of my thinking about this, which I am presenting next week at NHSM.  I would love to have an infographic to share as part of that.   I am still finalizing the exact content, but you can get the gits of what I have in mind in my last two blog posts at www.craftingpartners.net/blog 

The info grpahic will be made up mainly of the material in the two small charts, one in each post, which will be combined along with some additional information. I will attempt to post the completed, or at least near completed, content soon.

Thanks for your ideas for this graphic.  I plan to submit it to some high profile blogs like Tinklepost, and will include a designed credit as part of that.

The infographic I have in mind, will have at least two versions.  The first will be more basic, and will consist of the content in the spreadsheet as laid out in the two part in my blog posts of 2/7 and 2/27 at www.craftingpartners.net/blog.  The second will build on and extend this initial graphic, with the addition of at least one major row, and a number of additional columns.  One key addition is going to be a list of tools and technologies in each of these areas.

I will try to find a way to share these working drafts as attachments here so that you can review them as you work up ideas for this.  Given that some of this will see the light of day at NHSM next week, I look forward to hearing from you soon, and am looking to make a quick decision on who to work with.

Thanks!
Martin Feltner
martin@craftingpartners.net

Reason: I would love to give a chance for some designs to come in on this. i appreciate whatever you can send my way.

Thanks for the comments about my project.  I have just posted an update to make it clearer what I am looking for in this illustration.  Please check out the attached Excel worksheet with two tabs, one for the short version, and one for the longer version, presumably in the same graphic style.  And my blog posts at www.craftingpartners.net/blog can give you a little more background on my direction if you need it.  Please keep questions coming-I am back from travelling and will respond quickly.  Thanks for your submissions.

Target Market(s)

Business professionals

Industry/Entity Type

Industry

Requirements
Must have
• clean and readable, attractive and impactful online

needs to expandable-the grid will have additional rows and columns to it added over time
Nice to have
• needs to look good printed as well as online

```html
<!DOCTYPE html>
<html lang="en">
<head>
<meta charset="utf-8">
<title>The Event Graph</title>
<link rel="stylesheet" href="https://fonts.googleapis.com/css2?family=Arimo:wght@400;700&display=swap">
<style>
  :root {
    --bg-center: #ffe25a;
    --bg-mid: #ffc640;
    --bg-edge: #f7a33a;
    --title-red: #e4202a;
    --title-dark: #b3121c;
    --band-purple: #8b2a83;
    --head-purple: #7a3aa6;
    --head-purple-dark: #4f1d78;
    --head-red: #e3262f;
    --head-red-dark: #a7121a;
    --cell-yellow: #fff6a8;
    --cell-yellow-edge: #f6d860;
    --cell-pink: #ffd6ec;
    --cell-pink-edge: #f39acb;
    --cell-border: #e9952f;
    --ink: #5b2a8c;
    --rule: #fff4d2;
    --art-blue: #5fb3e8;
    --art-pink: #f06aa8;
    --art-gold: #f2b233;
    --art-green: #9acb5a;
  }
  * { box-sizing: border-box; margin: 0; padding: 0; }
  html, body { width: 1200px; height: 776px; overflow: hidden; }
  body {
    font-family: "Arimo", Arial, sans-serif;
    background: radial-gradient(ellipse 60% 55% at 50% 42%, var(--bg-center) 0%, var(--bg-mid) 55%, var(--bg-edge) 100%);
    position: relative;
    color: var(--ink);
  }
  .title {
    position: absolute; top: 60px; left: 0; width: 100%;
    text-align: center; font-weight: 700; font-size: 70px; letter-spacing: -1px;
    color: var(--title-red);
    text-shadow: 0 2px 0 var(--title-dark), 0 0 2px #fff, 0 0 3px #fff;
  }
  .tagline {
    position: absolute; top: 169px; left: 145px; width: 918px; height: 30px;
    border-radius: 15px;
    background: linear-gradient(#a8399f, var(--band-purple));
    color: #fff; font-size: 19.5px; letter-spacing: 0.6px;
    display: flex; align-items: center; justify-content: center;
  }
  .grid {
    position: absolute; left: 19px; top: 226px;
    display: grid;
    grid-template-columns: repeat(8, 136px);
    column-gap: 11px;
    grid-template-rows: 78px 24px 106px 28px 106px 30px 106px 26px;
  }
  .rule { grid-column: 1 / -1; align-self: center; height: 5px; border-radius: 3px; background: var(--rule); opacity: .9; }
  .head {
    border-radius: 8px; color: #fff; font-size: 11.5px; line-height: 1.2;
    display: flex; align-items: center; justify-content: center; text-align: center; padding: 5px 8px;
    box-shadow: 0 2px 4px rgba(120,50,0,.35);
  }
  .head--purple { background: linear-gradient(#9a55c6, var(--head-purple) 55%, var(--head-purple-dark)); }
  .head--red { background: linear-gradient(#f04a50, var(--head-red) 55%, var(--head-red-dark)); }
  .cell {
    border-radius: 10px; border: 2px solid var(--cell-border);
    box-shadow: 0 2px 4px rgba(120,50,0,.35);
    font-size: 12px; line-height: 1.2; text-align: center;
    display: flex; flex-direction: column; align-items: center; justify-content: center; gap: 6px;
    padding: 6px 8px;
  }
  .cell--yellow { background: radial-gradient(circle at 50% 40%, #fffde0, var(--cell-yellow) 60%, var(--cell-yellow-edge)); }
  .cell--pink { background: radial-gradient(circle at 50% 40%, #fff0f8, var(--cell-pink) 60%, var(--cell-pink-edge)); }
  .cell--small { font-size: 9.5px; line-height: 1.24; padding: 6px 10px; }
  .art { border-radius: 6px; flex: none; }
  .art--people { background: linear-gradient(var(--art-blue), #2c7fc4); }
  .art--crowd-red { background: linear-gradient(#e0443c, #9f1515); }
  .art--bubbles { background: linear-gradient(#c9a7d8, #8fc4ec); }
  .art--presenter { background: linear-gradient(var(--art-pink), #f9c4de); }
  .art--notes { background: linear-gradient(90deg, var(--art-pink), #c2187a); }
  .art--money { background: linear-gradient(var(--art-green), #e6d37a); }
  .art--trucks { background: linear-gradient(#e2e2e2, var(--art-gold)); }
  .art--sponsor { background: linear-gradient(var(--art-gold), var(--art-blue)); }
  .art--cash { background: linear-gradient(#f5d36a, #caa035); }
  .art--senses { background: linear-gradient(90deg, var(--art-blue), #3a79c3); }
  .art--trio { background: linear-gradient(90deg, #e2504a, #f2b233, #3d6fb7); }
  .art--interest { background: linear-gradient(#8fcbf0, #3f94d6); }
  .art--social { background: linear-gradient(#bfe4f8, #5aa9e0); }
  .brands { display: flex; flex-wrap: wrap; justify-content: center; align-items: center; gap: 4px 10px; font-weight: 700; font-size: 12px; }
  .brand { display: inline-flex; align-items: center; gap: 3px; }
  .brand-dot { width: 9px; height: 9px; border-radius: 50%; background: var(--ink); }
</style>
</head>
<body>
  <h1 class="title">The Event Graph</h1>
  <p class="tagline">Our social graph and interest graph, as brought to life via business events.</p>

  <main class="grid">
    <div class="head head--purple">Event Dimensions:</div>
    <div class="head head--red">The three Keys to success in the new world of events:</div>
    <div class="head head--purple">The three key challenges to be overcome/How Events are currently broken:</div>
    <div class="head head--red">Relationship to Interest and Social Graph:</div>
    <div class="head head--purple">Event Elements:</div>
    <div class="head head--red">Main Participants:</div>
    <div class="head head--purple">Functions:</div>
    <div class="head head--red">How is this need also being met in our lives today, outside of events?</div>

    <div class="rule"></div>

    <div class="cell cell--yellow">The Content presented and the Learning received</div>
    <div class="cell cell--pink">
      <div class="art art--senses" role="img" aria-label="Small icons of a speaker, an ear and an eye" style="width:70px;height:16px"></div>
      Prioritize where to invest our attention
    </div>
    <div class="cell cell--yellow">We as an audience are overwhelmed
      <div class="art art--people" role="img" aria-label="Three small blue audience figures" style="width:56px;height:26px"></div>
    </div>
    <div class="cell cell--pink">
      <div class="art art--interest" role="img" aria-label="Growth chart illustration for the interest graph" style="width:84px;height:50px"></div>
      The Interest Graph
    </div>
    <div class="cell cell--yellow">Program Sessions
      <div class="art art--presenter" role="img" aria-label="Presenter at a lectern beside a screen" style="width:104px;height:50px"></div>
    </div>
    <div class="cell cell--pink">Speakers, entertainment
      <div class="art art--notes" role="img" aria-label="Music notes and a treble clef" style="width:84px;height:30px"></div>
    </div>
    <div class="cell cell--yellow cell--small">Inform/inspire others, but also to focus and galvanize the speakers own thinking; and to enhance their own status; at its highest to unify and transcend</div>
    <div class="cell cell--pink">Web content, clipstream, ideastage talks, etc...
      <div class="brands">
        <span class="brand"><span class="brand-dot"></span>ClipStream</span>
        <span class="brand">IdeaStage</span>
      </div>
    </div>

    <div class="rule"></div>

    <div class="cell cell--yellow">
      <div class="art art--crowd-red" role="img" aria-label="Silhouettes of a group of business people" style="width:60px;height:48px"></div>
      The networking and connections that take place
    </div>
    <div class="cell cell--pink">Identify and meet with the best potential contacts</div>
    <div class="cell cell--yellow">
      <div class="art art--bubbles" role="img" aria-label="Overlapping speech bubbles" style="width:56px;height:44px"></div>
      Networking is haphazard
    </div>
    <div class="cell cell--pink">The Social Graph
      <div class="art art--social" role="img" aria-label="Segmented chart illustration for the social graph" style="width:70px;height:46px"></div>
    </div>
    <div class="cell cell--yellow">Networking<br>breaks<br>&amp; reception</div>
    <div class="cell cell--pink">Audience
      <div class="art art--people" role="img" aria-label="Row of blue audience figures" style="width:96px;height:34px"></div>
    </div>
    <div class="cell cell--yellow">Learn, connect/share
      <div class="art art--trio" role="img" aria-label="Three business people side by side" style="width:84px;height:42px"></div>
    </div>
    <div class="cell cell--pink">
      <div class="brands">
        <span class="brand"><span class="brand-dot"></span>Chirply</span>
        <span class="brand">Friendloop</span>
        <span class="brand">Snapfolio</span>
      </div>
      Social networks, crm systems
    </div>

    <div class="rule"></div>

    <div class="cell cell--yellow">The lasting business impact which results
      <div class="art art--money" role="img" aria-label="Money bags, coins and banknotes" style="width:62px;height:48px"></div>
    </div>
    <div class="cell cell--pink">Integrate what we learn and who we meet with our ongoing business and lives</div>
    <div class="cell cell--yellow">We fail to tap the potential events have for lasting impact</div>
    <div class="cell cell--pink">The combination of The Interest Graph &amp; the Social Graph, as brought to life around a particular B to B event</div>
    <div class="cell cell--yellow">
      <div class="art art--trucks" role="img" aria-label="Delivery truck with money bags" style="width:104px;height:50px"></div>
      Marketplaces
    </div>
    <div class="cell cell--pink">Sponsors/Exhibits
      <div class="art art--sponsor" role="img" aria-label="Business person with a briefcase" style="width:44px;height:46px"></div>
    </div>
    <div class="cell cell--yellow">Consider/decide/buy
      <div class="art art--cash" role="img" aria-label="Stack of banknotes" style="width:64px;height:36px"></div>
    </div>
    <div class="cell cell--pink">
      <div class="brands">
        <span class="brand">Seekwell</span>
        <span class="brand">Rivermart</span>
      </div>
      Web advertising, ecommerce networks
      <div class="brands"><span class="brand">Bidstall</span></div>
    </div>

    <div class="rule"></div>
  </main>
</body>
</html>
```